Powerpoint Design for business and consulting company - Dorneck-Saalig

I am searching a design specialist who can help me to create a PowerPoint Design for my company. I'm in the business coaching and consulting industry.

The PPT master should be easy to use and include professional formatting (using the fonts of my website). In general, the slide master should have the look and feel of my website (in terms of fonts, colors, logos, possibility to place big photographs, having text and graph slides as well as photo slides with just 1 key message).

The PowerPoint design should fit my cooperate Identity (please see my website https://dorneck-saalig.de).
My logos are attached.

Additional information:
- wide screen format - 16: 9
- right set up of a fitting color scheme
https: // farbwexo. io / f6ded1-bfcbce-807f84-9cd3d1-666666
# 666666 (Dim Gray) - body / heading text
# 807F84 (Gray Web)
#BFCBCE (Silver Sand) - link hover
# 9cd3d1 (Powder Blue) - Link color
# F6DED1 (Champagne Pink)

- creation of chart templates, using chart tools, and different chart types etc.
- creation of different slide layouts to place content, pictures (in different sizes), optionally Media
- set up of display guide lines
- as well as standard elements, such as text boxes, lines, default shapes, etc.

Requirements
Must have
• Powerpoint Design needs to have:
https://farbwexo.io/f6ded1-bfcbce-807f84-9cd3d1-666666
# 807F84 (Gray Web)
# F6DED1 (Champagne Pink)

```html
<!DOCTYPE html>
<html lang="en">
<head>
<meta charset="utf-8">
<title>Dorneck-Saalig – Presentation Master</title>
<link href="https://fonts.googleapis.com/css2?family=Montserrat:wght@400;500;600;700&family=Open+Sans:wght@400;600;700&display=swap" rel="stylesheet">
<style>
:root{
  --dim:#666666;
  --gray:#807f84;
  --sand:#bfcbce;
  --teal:#9cd3d1;
  --teal-deep:#7fc3c1;
  --pink:#f6ded1;
  --tint:#eaf4f4;
  --pink-soft:#fbe9e0;
  --canvas:#ebecee;
  --white:#ffffff;
}
*{box-sizing:border-box;margin:0;padding:0}
html,body{width:1200px;height:2309px;overflow:hidden}
body{background:var(--canvas);position:relative;font-family:'Open Sans',sans-serif;color:var(--dim)}
.hero-band{position:absolute;left:0;top:0;width:1200px;height:700px}
.hero-brand{position:absolute;top:46px;left:0;width:1200px;text-align:center;font:500 30px 'Montserrat',sans-serif;color:var(--white);letter-spacing:.5px}
.hero-slide{position:absolute;left:281px;top:150px;width:639px;height:358px;box-shadow:0 12px 30px rgba(0,0,0,.35)}
.hero-slide .slide{transform:scale(1.8);transform-origin:0 0;box-shadow:none}

.deck{position:absolute;left:40px;top:726px;display:grid;grid-template-columns:repeat(3,355px);grid-auto-rows:199px;column-gap:27px;row-gap:27px}
.slide{position:relative;width:355px;height:199px;background:var(--white);overflow:hidden;box-shadow:0 2px 5px rgba(0,0,0,.18);font-size:6px;line-height:1.35;color:var(--dim)}
.abs{position:absolute}
.layer{position:absolute;left:0;top:0;width:100%;height:100%}
.s-title{position:absolute;left:18px;top:9px;font:500 11.5px 'Montserrat',sans-serif;color:var(--teal)}
.s-rule{position:absolute;left:0;right:0;top:27px;height:1px;background:var(--pink)}
.mark{position:absolute;left:18px;bottom:7px;font:600 6px 'Montserrat',sans-serif;color:var(--dim)}
.mark.light{color:var(--white)}
.pg{position:absolute;right:10px;bottom:7px;font-size:4px;color:var(--gray)}
.h-sm{font:600 7px 'Open Sans',sans-serif;color:var(--dim)}
.bul{list-style:none}
.bul li{position:relative;padding-left:8px;margin-top:2px}
.bul li::before{content:"";position:absolute;left:1px;top:3px;width:3px;height:3px;border-radius:50%;background:var(--teal)}
.bul li.sub{padding-left:22px}
.bul li.sub::before{left:15px;width:4px;height:1px;border-radius:0;top:4px;background:var(--gray)}
.side{position:absolute;left:217px;top:38px;width:125px}
.tint-panel{position:absolute;left:203px;top:28px;right:0;bottom:0;background:var(--tint)}
.chart-head{position:absolute;top:40px;font:500 7.5px 'Open Sans',sans-serif;text-align:center}

.t-title{position:absolute;left:13px;top:74px;font:500 13px/1.22 'Montserrat',sans-serif}
.t-sub{position:absolute;left:13px;top:113px;font:400 8px 'Montserrat',sans-serif}
.t-dash{position:absolute;left:13px;top:70px;width:12px;height:1.5px}

.toc-row{position:absolute;left:175px;width:162px;height:23px;border-bottom:1px solid var(--pink);font-size:5.8px;display:flex;align-items:flex-end;padding-bottom:3px}
.toc-row b{font:600 7px 'Montserrat',sans-serif;margin-right:4px;color:var(--dim)}
.lst{position:absolute;left:18px;width:320px;height:19px;display:flex;align-items:center;font-size:4.6px;padding-left:6px}
.lst svg{width:12px;height:12px;margin-right:6px}
.svc{position:absolute;top:52px;width:70px;text-align:center;font-size:3.8px;line-height:1.3}
.svc b{display:block;font-size:5px;color:var(--dim);margin:4px 0 2px}
.tbl{position:absolute;left:18px;top:38px;width:320px;border-collapse:collapse;font-size:3.6px;line-height:1.25}
.tbl th{font-size:5px;font-weight:700;text-align:center;padding:2px 0}
.tbl th.band{background:var(--teal);color:var(--white);font-weight:600}
.tbl td{vertical-align:top;padding:3px 3px;border-bottom:1px solid var(--sand);width:25%}
.qbox{position:absolute;top:38px;width:145px;height:80px;border:1px solid var(--pink);font-size:4px;line-height:1.3;text-align:center;padding:5px 7px}
.qmark{position:absolute;font:700 14px 'Montserrat',sans-serif;color:var(--pink);line-height:1}
.person{position:absolute;top:128px;width:110px;text-align:center;font-size:3.8px;line-height:1.25}
.person .av{width:20px;height:20px;border-radius:50%;margin:0 auto 3px;background:radial-gradient(circle at 50% 40%,#d8c3b4,#8b7c74)}
.person b{display:block;color:var(--teal);font-size:4.5px;font-weight:600}
.chev{position:absolute;top:100px;height:24px;font-size:4px;padding:3px 0 0 5px;line-height:1.25}
.chev b{display:block;font-size:5px}
.tl-note{position:absolute;font-size:3.8px;line-height:1.25;width:80px}
.stat{position:absolute;top:100px;width:70px;text-align:center;font-size:4px}
.stat b{display:block;color:var(--teal);font-size:5px;font-weight:600;margin-top:3px}
</style>
</head>
<body>

<svg class="hero-band" viewBox="0 0 1200 700" aria-hidden="true">
  <path d="M0 0H1200V350Q600 620 0 350Z" fill="#666666"/>
</svg>
<div class="hero-brand">Dorneck-Saalig</div>

<div class="hero-slide">
  <div class="slide">
    <svg class="layer" viewBox="0 0 355 199">
      <defs><linearGradient id="hphoto" x1="0" y1="0" x2="1" y2="1"><stop offset="0" stop-color="#8e8a86"/><stop offset=".5" stop-color="#b9ada4"/><stop offset="1" stop-color="#6f6a66"/></linearGradient></defs>
      <rect width="355" height="199" fill="url(#hphoto)" role="img" aria-label="Photo of the coach seated on stone steps, orange blazer"/>
      <path d="M148 0Q213 60 213 199" fill="none" stroke="#9cd3d1" stroke-width="5"/>
      <path d="M0 0H140Q205 60 205 199H0Z" fill="#666666"/>
    </svg>
    <div class="t-dash" style="background:var(--teal)"></div>
    <div class="t-title" style="color:var(--pink)">Presentation<br>Title Here</div>
    <div class="t-sub" style="color:var(--white)">Sub Heading Title</div>
    <div class="mark light" style="font-size:7px">Dorneck-Saalig</div>
  </div>
</div>

<main class="deck">

  <!-- 1 title dark -->
  <section class="slide">
    <svg class="layer" viewBox="0 0 355 199">
      <defs><linearGradient id="p1" x1="0" y1="0" x2="1" y2="1"><stop offset="0" stop-color="#8e8a86"/><stop offset=".5" stop-color="#b9ada4"/><stop offset="1" stop-color="#6f6a66"/></linearGradient></defs>
      <rect width="355" height="199" fill="url(#p1)" role="img" aria-label="Photo of the coach seated on stone steps, orange blazer"/>
      <path d="M148 0Q213 60 213 199" fill="none" stroke="#9cd3d1" stroke-width="5"/>
      <path d="M0 0H140Q205 60 205 199H0Z" fill="#666666"/>
    </svg>
    <div class="t-dash" style="background:var(--teal)"></div>
    <div class="t-title" style="color:var(--pink)">Presentation<br>Title Here</div>
    <div class="t-sub" style="color:var(--white)">Sub Heading Title</div>
    <div class="mark light" style="font-size:7px">Dorneck-Saalig</div>
  </section>

  <!-- 2 title teal -->
  <section class="slide">
    <svg class="layer" viewBox="0 0 355 199">
      <defs><linearGradient id="p2" x1="0" y1="0" x2="1" y2="1"><stop offset="0" stop-color="#9a9a9a"/><stop offset=".6" stop-color="#cfcfcf"/><stop offset="1" stop-color="#7a7a7a"/></linearGradient></defs>
      <rect width="355" height="199" fill="url(#p2)" role="img" aria-label="Black and white photo of the coach sitting outdoors"/>
      <path d="M148 0Q213 60 213 199" fill="none" stroke="#dcdcdc" stroke-width="5"/>
      <path d="M0 0H140Q205 60 205 199H0Z" fill="#9cd3d1"/>
    </svg>
    <div class="t-dash" style="background:var(--white)"></div>
    <div class="t-title" style="color:var(--white)">Presentation<br>Title Here</div>
    <div class="t-sub" style="color:var(--white)">Sub Heading Title</div>
    <div class="mark light" style="font-size:7px">Dorneck-Saalig</div>
  </section>

  <!-- 3 title photo top -->
  <section class="slide">
    <div class="abs" role="img" aria-label="Photo of the coach sitting on steps, laughing" style="left:0;top:0;width:355px;height:155px;background:linear-gradient(120deg,#8c8782,#c2b4a8 55%,#766f6a)"></div>
    <div class="abs" style="left:40px;top:167px;font:500 10px 'Montserrat',sans-serif;color:var(--teal)">Presentation Title Here</div>
    <div class="abs" style="left:40px;top:182px;font:500 7px 'Montserrat',sans-serif">Sub Heading Title</div>
    <div class="abs" style="right:14px;top:172px;font:600 7px 'Montserrat',sans-serif">Dorneck-Saalig</div>
  </section>

  <!-- 4 toc -->
  <section class="slide">
    <div class="abs" role="img" aria-label="Dark photo of a person walking past a building" style="left:0;top:0;width:155px;height:199px;background:linear-gradient(160deg,#7c7a78,#5d5b5a 60%,#6d6a68)"></div>
    <div class="abs" style="left:24px;top:80px;font:500 10px 'Montserrat',sans-serif;color:var(--teal)">Table of Content</div>
    <div class="abs" style="left:24px;top:95px;width:108px;height:1px;background:var(--white)"></div>
    <svg class="abs" style="left:33px;top:95px" width="10" height="6" viewBox="0 0 10 6"><path d="M1 0L5 5L9 0" fill="none" stroke="#fff" stroke-width="1"/></svg>
    <div class="toc-row" style="top:38px"><b>01</b>Lorem ipsum dolor sit amet</div>
    <div class="toc-row" style="top:61px"><b>02</b>Lorem ipsum dolor sit amet</div>
    <div class="toc-row" style="top:84px"><b>03</b>Lorem ipsum dolor sit amet</div>
    <div class="toc-row" style="top:107px"><b>04</b>Lorem ipsum dolor sit amet</div>
    <div class="toc-row" style="top:130px;border:none"><b>05</b>Lorem ipsum dolor sit amet</div>
    <div class="mark light" style="font-size:5px">Dorneck-Saalig</div>
    <div class="pg">4</div>
  </section>

  <!-- 5 list -->
  <section class="slide">
    <div class="s-title">Presentation Title Here</div><div class="s-rule"></div>
    <div class="abs" style="left:18px;top:38px"><div class="h-sm">Lorem Ipsum</div><div style="font-size:5.5px">Sint brute at usu. Duo iisque appareat adversarium at.</div></div>
    <div class="lst" style="top:65px;background:var(--tint)"><svg viewBox="0 0 12 12"><rect x="3" y="1.5" width="6" height="9" rx="1" fill="none" stroke="#807f84" stroke-width=".7"/></svg>Lorem ipsum dolor sit amet, te ullum corpora delicata duo. Rebum insolens pri eu. No alia tota modus qui.</div>
    <div class="lst" style="top:90px;background:var(--pink-soft)"><svg viewBox="0 0 12 12"><circle cx="6" cy="6" r="4" fill="none" stroke="#807f84" stroke-width=".7"/></svg>Lorem ipsum dolor sit amet, te ullum corpora delicata duo. Rebum insolens pri eu. No alia tota modus qui.</div>
    <div class="lst" style="top:115px;background:var(--tint)"><svg viewBox="0 0 12 12"><circle cx="4" cy="6" r="2.5" fill="none" stroke="#807f84" stroke-width=".7"/><circle cx="8.5" cy="5" r="2" fill="none" stroke="#807f84" stroke-width=".7"/></svg>Lorem ipsum dolor sit amet, te ullum corpora delicata duo. Rebum insolens pri eu. No alia tota modus qui.</div>
    <div class="lst" style="top:140px;background:var(--pink-soft)"><svg viewBox="0 0 12 12"><path d="M3 3L6 6L9 3M6 6V10" fill="none" stroke="#807f84" stroke-width=".7"/><circle cx="3" cy="3" r="1" fill="#807f84"/><circle cx="9" cy="3" r="1" fill="#807f84"/><circle cx="6" cy="10" r="1" fill="#807f84"/></svg>Lorem ipsum dolor sit amet, te ullum corpora delicata duo. Rebum insolens pri eu. No alia tota modus qui.</div>
    <div class="mark" style="font-size:5px">Dorneck-Saalig</div><div class="pg">5</div>
  </section>

  <!-- 6 divider -->
  <section class="slide">
    <div class="abs" role="img" aria-label="Bright photo of the coach laughing in front of glass architecture" style="left:0;top:0;width:355px;height:170px;background:linear-gradient(110deg,#dfe6ea,#c9cfd3 45%,#d8cbc1 70%,#eef1f3)"></div>
    <svg class="layer" viewBox="0 0 355 199">
      <path d="M0 150Q90 175 180 160T355 150V199H0Z" fill="#fff"/>
      <path d="M0 148Q90 173 180 158T355 148" fill="none" stroke="#9cd3d1" stroke-width="2.5"/>
    </svg>
    <div class="abs" style="left:20px;top:162px;font:500 9px 'Montserrat',sans-serif;color:var(--teal)">Divider Presentation</div>
    <div class="abs" style="left:20px;top:174px;font:500 7px 'Montserrat',sans-serif">Sub Heading</div>
    <div class="abs" style="right:12px;top:178px;font:600 6.5px 'Montserrat',sans-serif">Dorneck-Saalig</div>
  </section>

  <!-- 7 two column -->
  <section class="slide">
    <div class="s-title">Two Column</div><div class="s-rule"></div>
    <div class="abs" style="left:18px;top:42px;width:150px">
      <div class="h-sm">Lorem Ipsum</div>
      <ul class="bul"><li>Lorem ipsum dolor sit amet, te ullum corpora delicata duo. Rebum insolens pri eu. No alia tota modus qui.</li><li class="sub">Sint brute at usu. Duo iisque appareat adversarium at.</li><li>Lorem ipsum dolor sit amet, te ullum corpora delicata duo. Rebum insolens pri eu. No alia tota modus qui.</li><li class="sub">Sint brute at usu. Duo iisque appareat adversarium at.</li></ul>
    </div>
    <div class="abs" style="left:185px;top:42px;width:152px">
      <div class="h-sm">Lorem Ipsum</div>
      <ul class="bul"><li>Lorem ipsum dolor sit amet, te ullum corpora delicata duo. Rebum insolens pri eu. No alia tota modus qui.</li><li class="sub">Sint brute at usu. Duo iisque appareat adversarium at.</li><li>Lorem ipsum dolor sit amet, te ullum corpora delicata duo. Rebum insolens pri eu. No alia tota modus qui.</li><li class="sub">Sint brute at usu. Duo iisque appareat adversarium at.</li></ul>
    </div>
    <div class="mark" style="font-size:5px">Dorneck-Saalig</div><div class="pg">7</div>
  </section>

  <!-- 8 left column -->
  <section class="slide">
    <div class="s-title">Left Column</div><div class="s-rule" style="right:160px"></div>
    <div class="abs" role="img" aria-label="Photo of hands holding a tablet over a desk" style="left:193px;top:0;width:162px;height:199px;background:linear-gradient(150deg,#e4e1dc,#c4b7a8 50%,#8e8a86)"></div>
    <div class="abs" style="left:18px;top:42px;width:155px">
      <div class="h-sm">Lorem Ipsum</div>
      <ul class="bul"><li>Lorem ipsum dolor sit amet, te ullum corpora delicata duo. Rebum insolens pri eu. No alia tota modus qui.</li><li class="sub">Sint brute at usu. Duo iisque appareat adversarium at.</li><li>Lorem ipsum dolor sit amet, te ullum corpora delicata duo. Rebum insolens pri eu. No alia tota modus qui.</li><li class="sub">Sint brute at usu. Duo iisque appareat adversarium at.</li></ul>
    </div>
    <div class="mark" style="font-size:5px">Dorneck-Saalig</div>
  </section>

  <!-- 9 about us -->
  <section class="slide">
    <div class="s-title">About Us</div><div class="s-rule"></div>
    <div class="abs" role="img" aria-label="Photo of the coach resting her chin on her hand beside plants" style="left:0;top:28px;width:133px;height:171px;background:linear-gradient(140deg,#d9d6d0,#b8aa9c 50%,#6f6a64)"></div>
    <svg class="abs" style="left:20px;top:28px" width="10" height="6" viewBox="0 0 10 6"><path d="M0 0L5 5L10 0Z" fill="#fff"/></svg>
    <div class="abs" style="left:25px;top:128px;width:104px;padding:4px 6px;background:rgba(156,211,209,.92);color:var(--white);font-size:5.5px;font-style:italic;line-height:1.3">“Lorem ipsum dolor sit amet, te ullum corpora delicata duo.”</div>
    <div class="abs" style="left:160px;top:44px;width:165px;font-size:6px;line-height:1.33">Lorem ipsum dolor sit amet, te ullum corpora delicata duo. Rebum insolens pri eu. No alia tota modus qui. Lorem ipsum dolor sit amet, te ullum corpora delicata duo. Rebum insolens pri eu. No alia tota modus qui. Lorem ipsum dolor sit amet, te ullum corpora delicata duo. Rebum insolens pri eu. No alia tota modus qui.<br>Lorem ipsum dolor sit amet, te ullum corpora delicata duo. Rebum insolens pri eu. No alia tota modus qui.</div>
    <div class="abs" style="right:20px;top:163px;text-align:right;font-size:5.5px;font-weight:700">Your <span style="color:var(--teal);font-weight:400">Name</span><div style="font-size:4px;font-weight:400">Your Title Job</div></div>
    <div class="mark light" style="font-size:5px">Dorneck-Saalig</div><div class="pg">9</div>
  </section>

  <!-- 10 service -->
  <section class="slide">
    <div class="s-title">Service &amp; Kooperation</div><div class="s-rule"></div>
    <div class="abs" style="left:0;right:0;top:38px;height:148px;background:var(--tint)"></div>
    <svg class="abs" style="left:0;top:38px" width="355" height="40" viewBox="0 0 355 40">
      <g fill="none" stroke="#9cd3d1" stroke-width="1.2">
        <circle cx="53" cy="20" r="18" fill="#fff"/><circle cx="136" cy="20" r="18" fill="#fff"/><circle cx="219" cy="20" r="18" fill="#fff"/><circle cx="302" cy="20" r="18" fill="#fff"/>
      </g>
      <g fill="none" stroke="#807f84" stroke-width=".7">
        <rect x="47" y="11" width="9" height="15" rx="1"/><rect x="52" y="14" width="7" height="11" rx="1"/>
        <circle cx="136" cy="18" r="8"/><path d="M128 18H144M136 10Q131 18 136 26Q141 18 136 10M131 30H141M136 26V30"/>
        <circle cx="215" cy="20" r="5"/><circle cx="215" cy="20" r="2"/><circle cx="224" cy="17" r="3.5"/><circle cx="224" cy="17" r="1.2"/>
        <circle cx="302" cy="20" r="2.5"/><circle cx="295" cy="13" r="1.8"/><circle cx="310" cy="13" r="1.8"/><circle cx="295" cy="27" r="1.8"/><circle cx="310" cy="27" r="1.8"/><path d="M300 18L296 14M304 18L309 14M300 22L296 26M304 22L309 26"/>
      </g>
    </svg>
    <div class="svc" style="left:18px;top:80px"><b>#Digital first</b>Coachings, Workshops &amp; Trainings biete ich nicht nur klassisch, sondern auch online an. Letzteres dann #Digital first gedacht! Von der Konzeption über die Durchführung bis hin zur Erfolgsanalyse.</div>
    <div class="svc" style="left:101px;top:80px"><b>#International</b>Je nach thematischem Schwerpunkt moderiere ich Workshops &amp; Trainings gerne in Englisch. Die Teilnehmer können dabei über mehrere globale Standorte verteilt und virtuell zugeschaltet sein.</div>
    <div class="svc" style="left:184px;top:80px"><b>#Customized</b>Meine Formate sind auf die Bedürfnisse und Gegebenheiten meiner Kunden angepasst. Entwicklungsprogramme entstehen in einem iterativen Prozess, der Flexibilität und gemeinsames Lernen erlaubt.</div>
    <div class="svc" style="left:267px;top:80px"><b>#Networks</b>Alleine bin ich stark – im Netzwerk noch stärker! Für umfangreiche Workshops-, Trainings-, Coaching oder Beratungsprojekte arbeite ich seit vielen Jahren vertrauensvoll mit den <u style="color:var(--teal)">Experten von link &amp; grow</u> in München.<br><span style="color:var(--teal);font-size:3.4px">link and grow</span></div>
    <div class="mark" style="font-size:5px">Dorneck-Saalig</div><div class="pg">10</div>
  </section>

  <!-- 11 bar chart vertical -->
  <section class="slide">
    <div class="s-title">Bar Chart Sample</div><div class="s-rule"></div>
    <div class="tint-panel"></div>
    <div class="chart-head" style="left:0;width:203px">Heading Here</div>
    <svg class="abs" style="left:18px;top:55px" width="180" height="110" viewBox="0 0 180 110">
      <g font-size="4" fill="#807f84" font-family="Open Sans,sans-serif">
        <text x="0" y="93">0</text><text x="0" y="78">1</text><text x="0" y="63">2</text><text x="0" y="48">3</text><text x="0" y="33">4</text><text x="0" y="18">5</text><text x="0" y="4">6</text>
      </g>
      <line x1="8" y1="91" x2="178" y2="91" stroke="#bfcbce" stroke-width=".5"/>
      <rect x="14" y="26" width="8" height="65" fill="#666"/><rect x="24" y="55" width="8" height="36" fill="#9cd3d1"/><rect x="34" y="60" width="8" height="31" fill="#807f84"/>
      <rect x="57" y="40" width="8" height="51" fill="#666"/><rect x="67" y="25" width="8" height="66" fill="#9cd3d1"/><rect x="77" y="50" width="8" height="41" fill="#807f84"/>
      <rect x="100" y="35" width="8" height="56" fill="#666"/><rect x="110" y="60" width="8" height="31" fill="#9cd3d1"/><rect x="120" y="45" width="8" height="46" fill="#807f84"/>
      <rect x="143" y="20" width="8" height="71" fill="#666"/><rect x="153" y="48" width="8" height="43" fill="#9cd3d1"/><rect x="163" y="10" width="8" height="81" fill="#807f84"/>
      <g font-size="4" fill="#807f84" font-family="Open Sans,sans-serif">
        <text x="17" y="99">Category 1</text><text x="60" y="99">Category 2</text><text x="103" y="99">Category 3</text><text x="146" y="99">Category 4</text>
        <rect x="45" y="104" width="3" height="3" fill="#666"/><text x="50" y="107">Series 1</text><rect x="76" y="104" width="3" height="3" fill="#9cd3d1"/><text x="81" y="107">Series 2</text><rect x="107" y="104" width="3" height="3" fill="#807f84"/><text x="112" y="107">Series 3</text>
      </g>
    </svg>
    <div class="side"><div class="h-sm">Lorem Ipsum</div><ul class="bul"><li>Lorem ipsum dolor sit amet, te ullum corpora delicata duo. Rebum insolens pri eu. No alia tota modus qui.</li><li class="sub">Sint brute at usu. Duo iisque appareat adversarium at.</li><li>Lorem ipsum dolor sit amet, te ullum corpora delicata duo. Rebum insolens pri eu. No alia tota modus qui.</li></ul></div>
    <div class="mark" style="font-size:5px">Dorneck-Saalig</div><div class="pg">11</div>
  </section>

  <!-- 12 bar chart horizontal -->
  <section class="slide">
    <div class="s-title">Bar Chart Sample</div><div class="s-rule"></div>
    <div class="tint-panel"></div>
    <div class="chart-head" style="left:0;width:203px">Heading Here</div>
    <svg class="abs" style="left:10px;top:55px" width="190" height="110" viewBox="0 0 190 110">
      <g font-size="4" fill="#807f84" font-family="Open Sans,sans-serif">
        <text x="0" y="13">Category 4</text><text x="0" y="36">Category 3</text><text x="0" y="59">Category 2</text><text x="0" y="82">Category 1</text>
      </g>
      <rect x="26" y="2" width="100" height="5" fill="#666"/><rect x="26" y="8" width="57" height="5" fill="#9cd3d1"/><rect x="26" y="14" width="70" height="5" fill="#807f84"/>
      <rect x="26" y="25" width="53" height="5" fill="#666"/><rect x="26" y="31" width="35" height="5" fill="#9cd3d1"/><rect x="26" y="37" width="70" height="5" fill="#807f84"/>
      <rect x="26" y="48" width="40" height="5" fill="#666"/><rect x="26" y="54" width="90" height="5" fill="#9cd3d1"/><rect x="26" y="60" width="50" height="5" fill="#807f84"/>
      <rect x="26" y="71" width="46" height="5" fill="#666"/><rect x="26" y="77" width="57" height="5" fill="#9cd3d1"/><rect x="26" y="83" width="85" height="5" fill="#807f84"/>
      <g font-size="4" fill="#807f84" font-family="Open Sans,sans-serif">
        <text x="25" y="97">0</text><text x="45" y="97">1</text><text x="65" y="97">2</text><text x="85" y="97">3</text><text x="105" y="97">4</text><text x="125" y="97">5</text><text x="145" y="97">6</text>
        <rect x="40" y="103" width="3" height="3" fill="#807f84"/><text x="45" y="106">Series 3</text><rect x="71" y="103" width="3" height="3" fill="#9cd3d1"/><text x="76" y="106">Series 2</text><rect x="102" y="103" width="3" height="3" fill="#666"/><text x="107" y="106">Series 1</text>
      </g>
    </svg>
    <div class="side"><div class="h-sm">Lorem Ipsum</div><ul class="bul"><li>Lorem ipsum dolor sit amet, te ullum corpora delicata duo. Rebum insolens pri eu. No alia tota modus qui.</li><li class="sub">Sint brute at usu. Duo iisque appareat adversarium at.</li><li>Lorem ipsum dolor sit amet, te ullum corpora delicata duo. Rebum insolens pri eu. No alia tota modus qui.</li></ul></div>
    <div class="mark" style="font-size:5px">Dorneck-Saalig</div><div class="pg">12</div>
  </section>

  <!-- 13 pie -->
  <section class="slide">
    <div class="s-title">Pie Chart Sample</div><div class="s-rule"></div>
    <div class="tint-panel"></div>
    <div class="chart-head" style="left:0;width:203px">Heading Here</div>
    <svg class="abs" style="left:20px;top:55px" width="170" height="115" viewBox="0 0 170 115">
      <path d="M83 45L83 10A35 35 0 0 1 115 59Z" fill="#666"/>
      <path d="M83 45L115 59A35 35 0 0 1 80 80Z" fill="#9cd3d1"/>
      <path d="M83 45L80 80A35 35 0 0 1 50 32Z" fill="#807f84"/>
      <path d="M83 45L50 32A35 35 0 0 1 83 10Z" fill="#f6ded1"/>
      <g font-size="7" font-family="Open Sans,sans-serif"><text x="57" y="35" fill="#666">4,5</text><text x="91" y="32" fill="#fff">4,3</text><text x="60" y="64" fill="#fff">3,5</text><text x="93" y="62" fill="#fff">2,5</text></g>
      <g font-size="4" fill="#807f84" font-family="Open Sans,sans-serif">
        <rect x="2" y="109" width="3" height="3" fill="#f6ded1"/><text x="7" y="112">Category 1</text><rect x="39" y="109" width="3" height="3" fill="#807f84"/><text x="44" y="112">Category 2</text><rect x="76" y="109" width="3" height="3" fill="#666"/><text x="81" y="112">Category 3</text><rect x="113" y="109" width="3" height="3" fill="#9cd3d1"/><text x="118" y="112">Category 4</text>
      </g>
    </svg>
    <div class="side"><div class="h-sm">Lorem Ipsum</div><ul class="bul"><li>Lorem ipsum dolor sit amet, te ullum corpora delicata duo. Rebum insolens pri eu. No alia tota modus qui.</li><li class="sub">Sint brute at usu. Duo iisque appareat adversarium at.</li><li>Lorem ipsum dolor sit amet, te ullum corpora delicata duo. Rebum insolens pri eu. No alia tota modus qui.</li></ul></div>
    <div class="mark" style="font-size:5px">Dorneck-Saalig</div><div class="pg">13</div>
  </section>

  <!-- 14 donut -->
  <section class="slide">
    <div class="s-title">Donat Chart Sample</div><div class="s-rule"></div>
    <div class="tint-panel"></div>
    <div class="chart-head" style="left:0;width:203px">Heading Here</div>
    <svg class="abs" style="left:20px;top:55px" width="170" height="115" viewBox="0 0 170 115">
      <path d="M83 12A30 30 0 0 1 112 50L99 46A16 16 0 0 0 83 28Z" fill="#666"/>
      <path d="M112 50A30 30 0 0 1 88 72L86 57A16 16 0 0 0 99 46Z" fill="#9cd3d1"/>
      <path d="M88 72A30 30 0 0 1 54 50L68 47A16 16 0 0 0 86 57Z" fill="#807f84"/>
      <path d="M54 50A30 30 0 0 1 83 12L83 28A16 16 0 0 0 68 47Z" fill="#f6ded1"/>
      <g font-size="4.5" font-family="Open Sans,sans-serif" fill="#fff"><text x="60" y="32" fill="#666">30%</text><text x="95" y="30">29%</text><text x="93" y="62">17%</text><text x="65" y="66">24%</text></g>
      <g font-size="4" fill="#807f84" font-family="Open Sans,sans-serif">
        <rect x="2" y="109" width="3" height="3" fill="#f6ded1"/><text x="7" y="112">Category 1</text><rect x="39" y="109" width="3" height="3" fill="#807f84"/><text x="44" y="112">Category 2</text><rect x="76" y="109" width="3" height="3" fill="#666"/><text x="81" y="112">Category 3</text><rect x="113" y="109" width="3" height="3" fill="#9cd3d1"/><text x="118" y="112">Category 4</text>
      </g>
    </svg>
    <div class="side"><div class="h-sm">Lorem Ipsum</div><ul class="bul"><li>Lorem ipsum dolor sit amet, te ullum corpora delicata duo. Rebum insolens pri eu. No alia tota modus qui.</li><li class="sub">Sint brute at usu. Duo iisque appareat adversarium at.</li><li>Lorem ipsum dolor sit amet, te ullum corpora delicata duo. Rebum insolens pri eu. No alia tota modus qui.</li></ul></div>
    <div class="mark" style="font-size:5px">Dorneck-Saalig</div><div class="pg">14</div>
  </section>

  <!-- 15 ueber mich -->
  <section class="slide">
    <div class="s-title">Über Mich</div><div class="s-rule" style="right:130px"></div>
    <div class="abs" role="img" aria-label="Portrait photo of the coach smiling, white background" style="left:215px;top:0;width:140px;height:199px;background:linear-gradient(90deg,#fff,#e6dcd3 35%,#c9b09b 65%,#f1ece8)"></div>
    <div class="qmark" style="left:18px;top:54px">“</div>
    <div class="abs" style="left:18px;top:72px;width:195px;font:600 9.5px/1.3 'Open Sans',sans-serif">Das Reisen in über <span style="color:var(--teal)">45 Ländern</span>, Leben und Arbeiten auf mehreren Kontinenten und die Begegnung mit faszinierenden Kulturen hat mich tief geprägt.</div>
    <div class="mark" style="font-size:5px">Dorneck-Saalig</div>
  </section>

  <!-- 16 table -->
  <section class="slide">
    <div class="s-title">Table Sample</div><div class="s-rule"></div>
    <table class="tbl">
      <tr><th class="band" colspan="4">LOREM IPSUM</th></tr>
      <tr><th>Lorem ipsum</th><th>Lorem ipsum 1</th><th>Lorem ipsum 2</th><th>Lorem ipsum 3</th></tr>
      <tr><td>• Lorem ipsum dolor sit amet, consectetur adipiscing elit.<br>• Quisque nec enim luctus, finibus leo vulputate.<br><br>• Lorem ipsum dolor sit amet, consectetur adipiscing elit.</td><td>• Lorem ipsum dolor sit amet, consectetur adipiscing elit.<br><br><br>• Lorem ipsum dolor sit amet, consectetur adipiscing elit.</td><td>• Lorem ipsum dolor sit amet, consectetur adipiscing elit.<br><br><br>• Lorem ipsum dolor sit amet, consectetur adipiscing elit.<br>• Quisque nec enim luctus, finibus leo vulputate.</td><td>• Lorem ipsum dolor sit amet, consectetur adipiscing elit.<br>• Quisque nec enim luctus, finibus leo vulputate.<br>• Lorem ipsum dolor sit amet, consectetur adipiscing elit.<br>• Quisque nec enim luctus, finibus leo vulputate.</td></tr>
      <tr><td>• Lorem ipsum dolor sit amet, consectetur adipiscing elit.<br><br>• Lorem ipsum dolor sit amet, consectetur adipiscing elit.</td><td>• Lorem ipsum dolor sit amet, consectetur adipiscing elit.<br><br>• Lorem ipsum dolor sit amet, consectetur adipiscing elit.</td><td>• Lorem ipsum dolor sit amet, consectetur adipiscing elit.<br><br>• Lorem ipsum dolor sit amet, consectetur adipiscing elit.</td><td>• Lorem ipsum dolor sit amet, consectetur adipiscing elit.<br><br>• Lorem ipsum dolor sit amet, consectetur adipiscing elit.</td></tr>
    </table>
    <div class="mark" style="font-size:5px">Dorneck-Saalig</div><div class="pg">15</div>
  </section>

  <!-- 17 quote light -->
  <section class="slide">
    <div class="s-title">Quote Sample</div><div class="s-rule"></div>
    <div class="qmark" style="left:13px;top:34px">“</div>
    <div class="qbox" style="left:22px">In both the conceptualization and the execution of our Leadership Program at Vantora, Helena was and is such a valuable source of support. With dedication, flexibility and her true passion for people she executed a remote training program for Managers and ensured that even in times of unprecedented challenges due to Corona, our Leadership Team formed solid networks and act as coaches to all our people.</div>
    <div class="qmark" style="left:163px;top:108px">”</div>
    <div class="qmark" style="left:177px;top:34px">“</div>
    <div class="qbox" style="left:187px">Ich habe die Zusammenarbeit mit Helena immer sehr geschätzt. Sie verliert das Wesentliche nie aus den Augen, kann mit Komplexität umgehen, arbeitet professionell und in top Qualität. Helena ist auch ein sehr umsichtiger Mensch mit viel Feingefühl und Empathie. Sie bezieht Menschen in ihre Themen mit Leichtigkeit ein – nimmt deren Perspektiven nicht nur wahr, sondern wertschätzt und integriert sie auch.</div>
    <div class="qmark" style="left:328px;top:108px">”</div>
    <div class="person" style="left:86px"><div class="av" role="img" aria-label="Portrait photo of the first reference"></div><b>Lukas Arnholt</b>Global Director Talent<br>&amp; Culture, Vantora GmbH</div>
    <div class="person" style="left:240px"><div class="av" role="img" aria-label="Portrait photo of the second reference"></div><b>Petra Weindl</b>COO Kaufwelt Digital</div>
    <div class="mark" style="font-size:5px">Dorneck-Saalig</div><div class="pg">17</div>
  </section>

  <!-- 18 quote dark -->
  <section class="slide" style="background:var(--dim);color:var(--white)">
    <div class="s-title">Quote Sample</div><div class="s-rule" style="background:var(--gray)"></div>
    <div class="qmark" style="left:13px;top:34px;color:var(--white)">“</div>
    <div class="qbox" style="left:22px;border-color:var(--teal)">In both the conceptualization and the execution of our Leadership Program at Vantora, Helena was and is such a valuable source of support. With dedication, flexibility and her true passion for people she executed a remote training program for Managers and ensured that even in times of unprecedented challenges due to Corona, our Leadership Team formed solid networks and act as coaches to all our people.</div>
    <div class="qmark" style="left:163px;top:108px;color:var(--white)">”</div>
    <div class="qmark" style="left:177px;top:34px;color:var(--white)">“</div>
    <div class="qbox" style="left:187px;border-color:var(--teal)">Ich habe die Zusammenarbeit mit Helena immer sehr geschätzt. Sie verliert das Wesentliche nie aus den Augen, kann mit Komplexität umgehen, arbeitet professionell und in top Qualität. Helena ist auch ein sehr umsichtiger Mensch mit viel Feingefühl und Empathie. Sie bezieht Menschen in ihre Themen mit Leichtigkeit ein – nimmt deren Perspektiven nicht nur wahr, sondern wertschätzt und integriert sie auch.</div>
    <div class="qmark" style="left:328px;top:108px;color:var(--white)">”</div>
    <div class="person" style="left:86px"><div class="av" role="img" aria-label="Portrait photo of the first reference"></div><b style="color:var(--white)">Lukas Arnholt</b>Global Director Talent<br>&amp; Culture, Vantora GmbH</div>
    <div class="person" style="left:240px"><div class="av" role="img" aria-label="Portrait photo of the second reference"></div><b style="color:var(--white)">Petra Weindl</b>COO Kaufwelt Digital</div>
    <div class="mark light" style="font-size:5px">Dorneck-Saalig</div><div class="pg" style="color:var(--white)">18</div>
  </section>

  <!-- 19 timeline -->
  <section class="slide">
    <div class="s-title">Timeline Sample</div><div class="s-rule"></div>
    <div class="abs" role="img" aria-label="Faint world map in the background" style="left:40px;top:40px;width:280px;height:145px;background:radial-gradient(ellipse at center,#f1f2f3,#fff 70%)"></div>
    <svg class="abs" style="left:18px;top:100px" width="325" height="24" viewBox="0 0 325 24">
      <g fill="#e2e4e5"><path d="M0 0H48L54 12L48 24H0Z"/><path d="M108 0H156L162 12L156 24H108L114 12Z"/><path d="M216 0H264L270 12L264 24H216L222 12Z"/></g>
      <g fill="#fae6dc"><path d="M54 0H102L108 12L102 24H54L60 12Z"/><path d="M162 0H210L216 12L210 24H162L168 12Z"/><path d="M270 0H318L324 12L318 24H270L276 12Z"/></g>
    </svg>
    <div class="chev" style="left:18px"><b>TEXT 1</b>Lorem ipsum dolor<br>sit amet</div>
    <div class="chev" style="left:78px"><b>TEXT 2</b>Lorem ipsum<br>dolor sit amet</div>
    <div class="chev" style="left:132px"><b>TEXT 3</b>Lorem ipsum<br>dolor sit amet</div>
    <div class="chev" style="left:186px"><b>TEXT 4</b>Lorem ipsum<br>dolor sit amet</div>
    <div class="chev" style="left:240px"><b>TEXT 5</b>Lorem ipsum<br>dolor sit amet</div>
    <div class="chev" style="left:294px"><b>TEXT 6</b>Lorem ipsum<br>dolor sit amet</div>
    <svg class="abs" style="left:0;top:0" width="355" height="199" viewBox="0 0 355 199"><g stroke="#807f84" stroke-width=".5"><line x1="75" y1="68" x2="75" y2="100"/><line x1="183" y1="68" x2="183" y2="100"/><line x1="291" y1="68" x2="291" y2="100"/><line x1="90" y1="124" x2="90" y2="152"/><line x1="198" y1="124" x2="198" y2="152"/><line x1="306" y1="124" x2="306" y2="152"/></g></svg>
    <div class="tl-note" style="left:40px;top:48px">Lorem ipsum dolor sit amet, te ullum corpora delicata duo. Rebum insolens pri eu.</div>
    <div class="tl-note" style="left:145px;top:48px">Lorem ipsum dolor sit amet, te ullum corpora delicata duo. Rebum insolens pri eu.</div>
    <div class="tl-note" style="left:253px;top:48px">Lorem ipsum dolor sit amet, te ullum corpora delicata duo. Rebum insolens pri eu.</div>
    <div class="tl-note" style="left:12px;top:155px;text-align:center">Lorem ipsum dolor sit amet, te ullum corpora delicata duo. Rebum insolens pri eu.</div>
    <div class="tl-note" style="left:120px;top:155px;text-align:center">Lorem ipsum dolor sit amet, te ullum corpora delicata duo. Rebum insolens pri eu.</div>
    <div class="tl-note" style="left:228px;top:155px;text-align:center">Lorem ipsum dolor sit amet, te ullum corpora delicata duo. Rebum insolens pri eu.</div>
    <div class="mark" style="font-size:5px">Dorneck-Saalig</div><div class="pg">19</div>
  </section>

  <!-- 20 image with data -->
  <section class="slide">
    <div class="s-title">Image with Data</div><div class="s-rule"></div>
    <div class="abs" role="img" aria-label="Soft-focus photo of a workshop with sticky notes and a phone" style="left:0;top:28px;width:355px;height:92px;background:linear-gradient(100deg,#aeb4bb,#d8d2d6 40%,#c7b8c6 65%,#8f8a94)"></div>
    <svg class="abs" style="left:0;top:95px" width="355" height="50" viewBox="0 0 355 50">
      <g fill="#fff"><circle cx="62" cy="22" r="22"/><circle cx="177" cy="22" r="22"/><circle cx="292" cy="22" r="22"/></g>
      <g fill="none" stroke-width="5">
        <circle cx="62" cy="22" r="16" stroke="#e3f2f2"/><circle cx="62" cy="22" r="16" stroke="#9cd3d1" stroke-dasharray="75.4 100.5" transform="rotate(-90 62 22)"/>
        <circle cx="177" cy="22" r="16" stroke="#fbe9e0"/><circle cx="177" cy="22" r="16" stroke="#f6ded1" stroke-dasharray="65.3 100.5" transform="rotate(-90 177 22)"/>
        <circle cx="292" cy="22" r="16" stroke="#e2e4e5"/><circle cx="292" cy="22" r="16" stroke="#666" stroke-dasharray="62.3 100.5" transform="rotate(-90 292 22)"/>
      </g>
      <g font-size="7" font-weight="700" text-anchor="middle" font-family="Open Sans,sans-serif"><text x="62" y="25" fill="#9cd3d1">75%</text><text x="177" y="25" fill="#f2c3ab">65%</text><text x="292" y="25" fill="#666">62%</text></g>
    </svg>
    <div class="stat" style="left:27px;top:146px"><b>LOREM IPSUM</b>Lorem ipsum dolor sit amet, te ullum corpora delicata duo.</div>
    <div class="stat" style="left:142px;top:146px"><b>LOREM IPSUM</b>Lorem ipsum dolor sit amet, te ullum corpora delicata duo.</div>
    <div class="stat" style="left:257px;top:146px"><b>LOREM IPSUM</b>Lorem ipsum dolor sit amet, te ullum corpora delicata duo.</div>
    <div class="mark" style="font-size:5px">Dorneck-Saalig</div><div class="pg">20</div>
  </section>

  <!-- 21 thank you -->
  <section class="slide" style="background:var(--dim);color:var(--white)">
    <svg class="layer" viewBox="0 0 355 199">
      <defs><linearGradient id="p21" x1="0" y1="0" x2="1" y2="1"><stop offset="0" stop-color="#c9c9c9"/><stop offset=".5" stop-color="#efefef"/><stop offset="1" stop-color="#9a9a9a"/></linearGradient></defs>
      <rect x="150" width="205" height="199" fill="url(#p21)" role="img" aria-label="Black and white portrait photo of the coach"/>
      <path d="M148 0Q213 60 213 199" fill="none" stroke="#f6ded1" stroke-width="4"/>
      <path d="M0 0H140Q205 60 205 199H0Z" fill="#666666"/>
    </svg>
    <div class="abs" style="left:13px;top:34px;font:500 13px 'Montserrat',sans-serif;color:var(--white)">Thank You</div>
    <div class="abs" style="left:13px;top:58px;width:150px;font-size:4.6px;line-height:1.3">Lorem Ipsum is simply dummy text of the printing and typesetting industry. Lorem Ipsum has been the industry's standard dummy text ever since the 1500s, when an unknown printer took a galley of type and scrambled it to make a type specimen book.</div>
    <svg class="abs" style="left:13px;top:100px" width="8" height="50" viewBox="0 0 8 50" fill="#fff">
      <rect x="0" y="1" width="7" height="5"/><path d="M0 1L3.5 4L7 1" stroke="#666" stroke-width=".6" fill="none"/>
      <rect x="0.5" y="18" width="6" height="6"/>
      <path d="M3.5 35C1.5 35 0.5 36.5 0.5 38C0.5 40 3.5 43 3.5 43C3.5 43 6.5 40 6.5 38C6.5 36.5 5.5 35 3.5 35Z"/><circle cx="3.5" cy="38" r="1" fill="#666"/>
    </svg>
    <div class="abs" style="left:27px;top:100px;font-size:4.6px;line-height:1">Lorem ipsum</div>
    <div class="abs" style="left:27px;top:118px;font-size:4.6px;line-height:1">Lorem ipsum</div>
    <div class="abs" style="left:27px;top:136px;font-size:4.6px;line-height:1">Lorem ipsum</div>
    <div class="mark light" style="font-size:7px">Dorneck-Saalig</div>
  </section>

</main>
</body>
</html>
```